Lumen Kinetics Web Design Project

We need to update our web design for our company. Lumen Kinetics™ is a series of Development (Training) Programs that we deliver both for the General Public as well as Corporate Business.

Much of the content needs a refresh but we are keen to get some thoughts now on design and layout, predominantly front page. Happy to take any comments on the content if you think that is relevant as well.

We might look to move the current video clip and bring a more generic 'inspirational' clip to the front page. A good example of this is www.mindcraftoz.example.au

Our courses have a very similar market to Gerald Whitcombe type courses ... both General Public and Corporate business.

Refer our website www.lumenkinetics.example.com

Target Market(s)

General Public as well as Corporate Business. Courses are designed for all. Gerald Whitcombe would be a good 'feel' for what we do.

Industry/Entity Type

Business

Requirements
Must have
• Must have a 'leading edge' type feel to it.
Must look professional.

```html
<!DOCTYPE html>
<html lang="en">
<head>
<meta charset="utf-8">
<title>Lumen Kinetics</title>
<link href="https://fonts.googleapis.com/css2?family=Open+Sans:wght@400;600&family=Arimo:wght@400;700&family=Walter+Turncoat&display=swap" rel="stylesheet">
<style>
  :root {
    --sky-top: #1a7fe0;
    --sky-mid: #3aa4f4;
    --sky-glow: #5cc0ff;
    --nav-bg: #e9e9ea;
    --nav-text: #8a8a8a;
    --nav-active: #2a94f2;
    --hero-dark: #0c3a86;
    --hero-light: #2f78e0;
    --feature-red: #c81a14;
    --feature-red-soft: #e0443a;
    --page: #f6eeee;
    --panel: #e6e6ee;
    --panel-edge: #c9c9d2;
    --link-blue: #1a3cf0;
    --link-sky: #1a7ff0;
    --ink: #222;
    --muted: #9a9a9a;
    --button-top: #3c6bff;
    --button-bottom: #0a2ee6;
    --footer: #2a5ef2;
    --white: #fff;
  }
  * { box-sizing: border-box; margin: 0; padding: 0; }
  html, body { width: 900px; height: 1200px; overflow: hidden; }
  body { background: var(--page); font-family: "Open Sans", sans-serif; color: var(--ink); position: relative; }

  .site-header {
    position: absolute; left: 0; top: 0; width: 900px; height: 172px;
    background: radial-gradient(ellipse 420px 160px at 450px 90px, var(--sky-glow), transparent 70%),
                linear-gradient(180deg, var(--sky-top), var(--sky-mid) 70%, #4fb4f8);
    color: var(--white);
  }
  .brand { position: absolute; left: 34px; top: 28px; display: flex; align-items: center; gap: 12px; }
  .brand-dot { width: 18px; height: 18px; border-radius: 50%; background: var(--white); }
  .brand-name { font-size: 40px; line-height: 42px; font-weight: 400; width: 230px; }
  .tagline { position: absolute; left: 332px; top: 26px; font-size: 17px; line-height: 23px; }
  .intro { position: absolute; left: 332px; top: 89px; font-size: 12px; line-height: 19px; width: 230px; }
  .top-links { position: absolute; right: 26px; top: 6px; font-size: 17px; }
  .search { position: absolute; left: 704px; top: 57px; display: flex; }
  .search-field { width: 132px; height: 20px; background: #eef6ff; }
  .search-button { width: 44px; height: 20px; background: #1e74ea; color: var(--white); font-size: 8px; line-height: 20px; text-align: center; }

  .main-nav {
    position: absolute; left: 0; top: 172px; width: 900px; height: 50px;
    background: linear-gradient(180deg, #f4f4f4, var(--nav-bg));
    border-top: 2px solid #d4d4d4; border-bottom: 2px solid #d4d4d4;
    font-size: 17px; color: var(--nav-text);
  }
  .main-nav span { position: absolute; top: 13px; }
  .main-nav .is-active { left: 22px; top: 0; width: 95px; height: 46px; background: var(--nav-active); color: var(--white); text-align: center; line-height: 46px; }
  .main-nav .is-strong { color: #555; font-family: "Arimo", sans-serif; }

  .hero {
    position: absolute; left: 0; top: 222px; width: 900px; height: 395px;
    background: radial-gradient(ellipse 500px 260px at 650px 300px, var(--hero-light), transparent 75%),
                linear-gradient(180deg, #1c4fa8, var(--hero-dark));
    color: var(--white); font-family: "Arimo", sans-serif;
  }
  .hero-feature {
    position: absolute; left: 82px; top: 72px; width: 205px; height: 205px;
    background: linear-gradient(160deg, var(--feature-red-soft), var(--feature-red));
  }
  .hero-title { position: absolute; left: 495px; top: 18px; font-size: 33px; font-weight: 400; }
  .hero-lead { position: absolute; left: 410px; top: 70px; width: 440px; font-size: 14.5px; line-height: 21px; font-weight: 700; }
  .hero-quote { position: absolute; left: 420px; top: 122px; width: 460px; text-align: center; font-family: "Walter Turncoat", sans-serif; font-size: 15px; line-height: 28px; text-transform: uppercase; }
  .hero-points { position: absolute; left: 426px; top: 192px; width: 390px; list-style: none; font-size: 14.5px; line-height: 20px; }
  .hero-points li::before { content: "• "; }
  .hero-cta {
    position: absolute; left: 561px; top: 345px; width: 139px; height: 45px;
    background: linear-gradient(180deg, #3a86ff, #1b5ee6); border: 3px solid #0d1f3d; border-radius: 8px;
    font-size: 12px; line-height: 39px; text-align: center;
  }

  .welcome {
    position: absolute; left: 10px; top: 617px; width: 874px; height: 153px;
    background: linear-gradient(180deg, #fff, var(--panel)); box-shadow: 0 4px 10px rgba(0,0,0,.18);
  }
  .welcome-brand { position: absolute; left: 24px; top: 34px; display: flex; align-items: center; gap: 10px; color: #8d8d8d; }
  .welcome-brand .brand-dot { background: #b4b4b4; }
  .welcome-brand .brand-name { font-size: 34px; line-height: 38px; width: 190px; }
  .welcome-title { position: absolute; left: 243px; top: 14px; font-size: 26px; font-weight: 400; }
  .welcome-title em { font-style: normal; color: var(--link-blue); }
  .welcome-text { position: absolute; left: 246px; top: 50px; width: 630px; font-size: 14px; line-height: 18px; letter-spacing: -0.2px; color: var(--muted); }

  .programs, .newsletter {
    position: absolute; top: 785px; height: 288px; background: var(--panel);
    border: 2px solid var(--panel-edge); box-shadow: 1px 2px 3px rgba(0,0,0,.15);
  }
  .programs { left: 17px; width: 381px; }
  .programs ul { list-style: none; padding: 8px 0 0 17px; font-size: 14px; line-height: 36px; }
  .programs .lead { color: var(--link-sky); }
  .programs .name, .programs .accent { color: var(--link-blue); }
  .read-more {
    position: absolute; left: 72px; top: 268px; width: 202px; height: 34px; border-radius: 5px;
    background: linear-gradient(180deg, var(--button-top), var(--button-bottom)); color: var(--white);
    font-size: 14px; line-height: 34px; text-align: center;
  }
  .newsletter { left: 402px; width: 479px; border-radius: 6px; text-align: center; }
  .newsletter h2 { margin-top: 9px; font-size: 19px; font-weight: 600; color: var(--link-blue); }
  .newsletter .rule { width: 262px; height: 2px; background: #bdbdbd; margin: 6px auto 0; }
  .newsletter p { margin-top: 6px; font-size: 12.5px; line-height: 17px; color: var(--muted); }
  .field { position: absolute; left: 139px; width: 181px; height: 24px; background: var(--white); border: 1px solid #d6d6d6; font-size: 9px; color: #999; text-align: left; padding-left: 8px; line-height: 22px; }
  .subscribe {
    position: absolute; left: 162px; top: 197px; width: 140px; height: 35px;
    background: linear-gradient(180deg, var(--button-top), var(--button-bottom)); color: var(--white);
    font-size: 17px; line-height: 35px;
  }

  .site-footer { position: absolute; left: 0; top: 1123px; width: 900px; height: 77px; background: var(--footer); color: var(--white); font-size: 12.5px; line-height: 16px; }
  .follow { position: absolute; left: 32px; top: 21px; display: flex; align-items: center; gap: 5px; }
  .follow .label { margin-right: 6px; }
  .social { width: 26px; height: 26px; border-radius: 4px; background: #5a8cf6; }
  .footer-address { position: absolute; left: 412px; top: 7px; }
  .footer-contact { position: absolute; left: 535px; top: 7px; }
  .footer-legal { position: absolute; left: 742px; top: 25px; }
</style>
</head>
<body>
  <header class="site-header">
    <div class="brand"><span class="brand-dot"></span><span class="brand-name">lumen kinetics</span></div>
    <p class="tagline">A new way of Thinking to<br>create a new way of being</p>
    <p class="intro">Lumen Kinetic delivers leading edge workshop , seminar and product in a fun and interactive way.</p>
    <nav class="top-links">About Us I Contact Us</nav>
    <div class="search"><div class="search-field"></div><div class="search-button">SEARCH</div></div>
  </header>

  <nav class="main-nav">
    <span class="is-active">Home</span>
    <span class="is-strong" style="left:147px">Lumen Kinetic</span>
    <span style="left:317px">Our Programs</span>
    <span style="left:477px">Events</span>
    <span style="left:574px">Our Products</span>
    <span style="left:722px">Articles &amp; Resource</span>
  </nav>

  <section class="hero">
    <div class="hero-feature" role="img" aria-label="Sticker graphic announcing something new"></div>
    <h1 class="hero-title">Lumen Kinetics</h1>
    <p class="hero-lead">Lumen Kinetics™ is a leading edge model which introduces a new lens to view yourself and the world you operate within.</p>
    <p class="hero-quote">"Lumen Kinetics™ is for everyone.<br>It's all about transformation and skills for life."</p>
    <ul class="hero-points">
      <li>Improve your health and wellbeing</li>
      <li>Create a new fun and healthy culture</li>
      <li>Learn new ways to manage stress and create balance in your life</li>
      <li>Enhance your communication skills and strengthen your relationships</li>
      <li>Learn new ways to Transform and create all that you have ever wanted.</li>
    </ul>
    <div class="hero-cta">CONTACT US</div>
  </section>

  <section class="welcome">
    <div class="welcome-brand"><span class="brand-dot"></span><span class="brand-name">lumen kinetics</span></div>
    <h2 class="welcome-title">Welcome To Our <em>Company</em> !</h2>
    <p class="welcome-text">Lorem ipsum dolor sit amet, consectetuer adipiscing elit, sed diam nonummy nibh euismod tincidunt ut laoreet dolore magna aliquam erat volutpat. Ut wisi enim ad minim veniam, quis nostrud exerci tation ullamcorper suscipit lobortis nisl ut aliquip ex ea commodo consequat. Duis autem vel eum iriure dolor</p>
  </section>

  <section class="programs">
    <ul>
      <li class="lead">Experience for Yourself</li>
      <li><span class="name">Lumen Kinetics™</span> for You</li>
      <li><span class="name">Lumen Kinetics™</span> for Children and Schools</li>
      <li><span class="name">Lumen Kinetics™</span> for Business</li>
      <li><span class="name">Lumen Kinetics™</span> for Animals</li>
      <li><span class="name">Lumen Kinetics™</span> for Community</li>
      <li class="accent">Become an Accredited Lumen Kinetics™ Practitioner</li>
    </ul>
    <div class="read-more">READ MORE</div>
  </section>

  <section class="newsletter">
    <h2>Sign Up To Our Newsletter</h2>
    <div class="rule"></div>
    <p>Add Your Email Address and Subscribe<br>to our monthly newsletter</p>
    <div class="field" style="top:96px">Name</div>
    <div class="field" style="top:129px">Email address</div>
    <div class="subscribe">Subscribe</div>
  </section>

  <footer class="site-footer">
    <div class="follow">
      <span class="label">Follow On</span>
      <span class="social" role="img" aria-label="Social profile link"></span>
      <span class="social" role="img" aria-label="Social profile link"></span>
      <span class="social" role="img" aria-label="Video channel link"></span>
      <span class="social" role="img" aria-label="Professional network link"></span>
    </div>
    <div class="footer-address">Address<br>---------<br>PO Box 418<br>Harbour Lane West</div>
    <div class="footer-contact">Vic 8010 Australia<br>Mob: +61 (0) 400 555 018<br>Phone: +61 (3) 9000 5521<br>Email: info@lumenkinetics.example.com</div>
    <div class="footer-legal">Copyright 2013</div>
  </footer>
</body>
</html>
```